Kelvar Systems Website

Website design for our company: Kelvar Systems.
The website should look fresh and IT focused. Please have a look at http://www.kelvarsystems.net.au/ for our current design. We want something fresh and new, professional looking, in WordPress so we can easily make changes.

Industry/Entity Type

It Company

```html
<!DOCTYPE html>
<html lang="en">
<head>
<meta charset="utf-8">
<title>Kelvar Systems</title>
<link href="https://fonts.googleapis.com/css2?family=Open+Sans:wght@300;400;600;700&display=swap" rel="stylesheet">
<style>
:root{
  --green:#1fae4b;
  --green-dark:#16913d;
  --ink:#333;
  --muted:#666;
  --dark:#2b2b2b;
  --bar:#3a3a3a;
  --page:#ededed;
  --white:#fff;
}
*{box-sizing:border-box;margin:0;padding:0}
html,body{width:833px;height:1200px;overflow:hidden}
body{font-family:"Open Sans",Arial,sans-serif;background:var(--page);color:var(--ink);position:relative}
.wrap{width:730px;margin:0 auto;position:relative}

/* hero */
.hero{position:relative;height:353px;background:radial-gradient(ellipse at 45% 70%,#3c4a4f 0%,#1d2427 45%,#0d1012 100%);overflow:hidden}
.hero-photo{position:absolute;left:150px;top:95px;width:300px;height:240px;background:radial-gradient(ellipse at center,#5f6d70 0%,#39454a 45%,rgba(20,26,28,0) 75%)}
.topbar{position:absolute;right:52px;top:10px;display:flex;align-items:center;gap:6px;color:var(--white);font-size:9px;letter-spacing:.5px}
.topbar .call b{color:var(--green);font-weight:700}
.social{width:12px;height:12px;border-radius:50%;background:#555;display:inline-block}
.brand{position:absolute;left:52px;top:0;width:72px;height:72px;background:var(--dark);display:flex;flex-direction:column;align-items:center;justify-content:center;gap:5px}
.brand-mark{width:36px;height:36px;background:var(--green)}
.brand-name{font-size:7.5px;color:var(--white);font-weight:600;letter-spacing:.3px}
.nav{position:absolute;right:52px;top:32px;display:flex;gap:14px;font-size:8.5px;font-weight:600;color:var(--white);letter-spacing:.4px}
.nav a{color:inherit;text-decoration:none;padding-bottom:4px}
.nav a.active{color:var(--green);border-bottom:2px solid var(--green)}
.hero-copy{position:absolute;left:462px;top:140px;width:260px;text-align:center}
.hero-copy h1{color:var(--green);font-weight:400;font-size:19px;line-height:1.2;letter-spacing:.5px;margin-bottom:14px}
.hero-copy p{color:var(--white);font-size:10.5px;line-height:1.45;padding:0 10px}
.arrow{position:absolute;top:166px;width:20px;height:20px;border-radius:50%;background:rgba(255,255,255,.85)}
.arrow.left{left:12px}.arrow.right{right:12px}
.arrow svg{display:block}

/* intro band */
.band{background:var(--green);height:28px;display:flex;align-items:center;justify-content:center;color:var(--white);font-size:8.6px;font-weight:600;letter-spacing:.2px}

/* sections */
.card{background:var(--white);margin-top:16px;height:297px}
.bar{background:var(--bar);color:var(--white);font-size:11px;font-weight:600;letter-spacing:.5px;height:30px;display:flex;align-items:center;padding-left:14px;width:48%}
.intro{padding:20px 14px 0;font-size:9px;line-height:1.6;color:var(--muted)}
.intro p+p{margin-top:8px}
.services{display:flex;gap:20px;padding:30px 14px 0}
.service{flex:1}
.service h3{font-size:11px;font-weight:400;color:var(--ink);letter-spacing:.4px;border-bottom:1px solid #ccc;padding-bottom:4px;margin-bottom:8px}
.service .body{display:flex;gap:8px}
.service .pic{width:74px;height:52px;flex:none}
.service p{font-size:8px;line-height:1.45;color:var(--muted)}
.more{display:block;margin:8px 0 0 auto;width:max-content;background:var(--green);color:var(--white);font-size:7px;font-weight:700;padding:4px 7px;letter-spacing:.3px}

.duo{display:flex;gap:24px;margin-top:84px}
.panel{flex:1;background:var(--white)}
.panel .bar{width:100%;background:var(--dark)}
.testimonial{background:var(--bar);color:#ddd;padding:16px 16px;font-size:8.5px;line-height:1.55;height:136px;position:relative}
.testimonial .who{position:absolute;left:16px;bottom:14px;font-size:7.5px;font-weight:600;color:var(--white)}
.testimonial .more{position:absolute;right:16px;bottom:10px;margin:0;background:#111}
.remote{background:var(--bar);height:136px;padding:22px 16px;position:relative;color:var(--white)}
.remote label{font-size:9px;display:block;margin-bottom:8px}
.remote .field{width:130px;height:18px;background:var(--white)}
.remote .go{display:inline-block;margin-top:8px;background:var(--dark);border:1px solid #555;font-size:7.5px;font-weight:700;padding:4px 10px}
.remote .pic{position:absolute;right:24px;top:14px;width:96px;height:108px;background:linear-gradient(160deg,#d9d9d9,#8a8a8a)}

.clients{background:var(--white);margin-top:70px;height:140px}
.clients .bar{width:48%}
.client-row{display:flex;justify-content:space-around;padding:34px 20px 0}
.client{display:flex;align-items:center;gap:6px}
.client .ico{width:34px;height:34px}
.client span{font-size:8px;font-weight:700;line-height:1.2;letter-spacing:.3px}
.c1 span{color:#c98a1a}.c2 span{color:#1f9bd8}.c3 span{color:#1fae4b}.c4 span{color:#d6262e}.c5 span{color:#2c7fc2}

.footer{position:absolute;left:0;bottom:0;width:100%;height:22px;background:var(--green);color:var(--white);font-size:8px;display:flex;align-items:center;justify-content:center}
</style>
</head>
<body>

<header class="hero">
  <div class="hero-photo" role="img" aria-label="Photo of an open laptop on a dark desk"></div>
  <div class="brand"><div class="brand-mark"></div><div class="brand-name">Kelvar Systems</div></div>
  <div class="topbar"><span class="call">CALL US : <b>1800 555 214</b></span><span class="social"></span><span class="social"></span><span class="social"></span></div>
  <nav class="nav">
    <a class="active" href="#">HOME</a><a href="#">ABOUT US</a><a href="#">SERVICES</a><a href="#">SUPPORTS</a><a href="#">CLIENTS</a><a href="#">TESTIMONIALS</a><a href="#">CONTACT US</a>
  </nav>
  <div class="hero-copy">
    <h1>HARDWARE NETWORKING<br>SERVICES</h1>
    <p>We Specialise in the Implementation of Centralised Terminal Services Networks Which Provide Significant Advantages over Traditional PC Peer- to-peer networks</p>
  </div>
  <span class="arrow left"><svg width="20" height="20" viewBox="0 0 20 20"><path d="M12 5 7 10l5 5" fill="none" stroke="#222" stroke-width="2"/></svg></span>
  <span class="arrow right"><svg width="20" height="20" viewBox="0 0 20 20"><path d="M8 5l5 5-5 5" fill="none" stroke="#222" stroke-width="2"/></svg></span>
</header>

<div class="band">KELVAR SYSTEMS IS AN ADELAIDE BASED COMPANY WITH A SINGLE OBJECTIVE - TO EXCEL IN THE SUPPORT AND SERVICE OF ALL COMPUTER AND IT NEEDS.</div>

<main class="wrap">
  <section class="card">
    <div class="bar">WHAT WE DO</div>
    <div class="intro">
      <p>We provide a high level of consulting services using the most experienced engineers at a reasonable and fair price. We believe in using a Business Values approach to every aspect of computer consulting to provide our clients with the most cost effective solutions.</p>
      <p>We strongly believe that we are in business with our clients. Everything we do must be measured against our clients' business objectives. At the end of the day our client's success is our success.</p>
    </div>
    <div class="services">
      <div class="service">
        <h3>NETWORKING</h3>
        <div class="body"><div class="pic" role="img" aria-label="Illustration of networked computers" style="background:linear-gradient(135deg,#cfe3f2,#7fa9c9)"></div>
        <p>We offer fully integrated and planned network designs, built to keep every office, team and device connected and running smoothly.</p></div>
        <a class="more" href="#">READ MORE</a>
      </div>
      <div class="service">
        <h3>SERVERS</h3>
        <div class="body"><div class="pic" role="img" aria-label="Photo of server racks" style="background:linear-gradient(135deg,#8fb6d6,#2f5d86)"></div>
        <p>We specialise in building, installing and managing server systems that give your business a secure home for data, mail and applications.</p></div>
        <a class="more" href="#">READ MORE</a>
      </div>
      <div class="service">
        <h3>SECURITY</h3>
        <div class="body"><div class="pic" role="img" aria-label="Photo illustrating computer security" style="background:linear-gradient(135deg,#b9c8d6,#55687a)"></div>
        <p>We set up, monitor and maintain protection across all of your IT systems, from firewalls and backups to software updates.</p></div>
        <a class="more" href="#">READ MORE</a>
      </div>
    </div>
  </section>

  <div class="duo">
    <section class="panel">
      <div class="bar">TESTIMONIALS</div>
      <div class="testimonial">
        <p>"I have always found the most extremely helpful team with their advice over the phone. They also have the ability to access our computers remotely, and can sort most problems quite swiftly. I have no hesitation to recommend Kelvar Systems for all of your IT needs."</p>
        <div class="who">Daniel Harwood (Director) Harwood Freight Pty Ltd, South Australia</div>
        <a class="more" href="#">READ MORE</a>
      </div>
    </section>
    <section class="panel">
      <div class="bar">REMOTE SUPPORT</div>
      <div class="remote">
        <label>Enter your 6 - digit code</label>
        <div class="field"></div>
        <span class="go">CONNECT NOW</span>
        <div class="pic" role="img" aria-label="Illustration of a computer with a first aid kit"></div>
      </div>
    </section>
  </div>

  <section class="clients">
    <div class="bar">OUR CLIENTS</div>
    <div class="client-row">
      <div class="client c1"><div class="ico" role="img" aria-label="Financial institutions icon" style="background:#e8c77a"></div><span>FINANCIAL<br>INSTITUTIONS</span></div>
      <div class="client c2"><div class="ico" role="img" aria-label="Insurance companies icon" style="background:#9fd3ee"></div><span>INSURANCE<br>COMPANIES</span></div>
      <div class="client c3"><div class="ico" role="img" aria-label="Pharmacies icon" style="background:#9fdcb2"></div><span>PHARMACIES<br>COMPANIES</span></div>
      <div class="client c4"><div class="ico" role="img" aria-label="Real estate icon" style="background:#efa0a3"></div><span>REAL ESTATE<br>INDUSTRIES</span></div>
      <div class="client c5"><div class="ico" role="img" aria-label="Charity organisations icon" style="background:#a5c8e6"></div><span>CHARITY<br>ORGANIZATIONS</span></div>
    </div>
  </section>
</main>

<footer class="footer">Copyright © 2013 Kelvar Systems Pty. Ltd. All Rights Reserved.</footer>
</body>
</html>
```